Logo & Visitenkarte für Immobilienunternehmen
Zielgruppe
Wir sind ein Immobilienunternehmen. Wir sind tätig im Immobilienhandel, der Immobilienvermittlung und der Erstellung von Häusern.
Unsere Zielgruppe sind Personen, die eine Immobilie kaufen oder verkaufen wollen. Personen ab ca. 30 Jahren mit mittlerem bis hohem Kapital bzw. Einkommen
Aufgabenstellung
Das Design soll für Sicherheit, Vertrauen, Seriosität, Professionalität und Hochwertigkeit stehen, da es in der Immobilienbranche oft um sehr viel Geld geht.

```html
<!DOCTYPE html>
<html lang="de">
<head>
<meta charset="utf-8">
<title>Ferbin Immobilien – Visitenkarte</title>
<link rel="stylesheet" href="https://fonts.googleapis.com/css2?family=Josefin+Sans:wght@400;700&display=swap">
<style>
  :root {
    --backdrop: #e9e9e9;
    --card: #817c73;
    --gold: #f2b43a;
    --gold-light: #f8c95a;
    --gold-deep: #d99a22;
    --shadow: rgba(0, 0, 0, 0.22);
  }
  * { margin: 0; padding: 0; box-sizing: border-box; }
  html, body { width: 1200px; height: 675px; overflow: hidden; }
  body {
    background: var(--backdrop);
    font-family: "Josefin Sans", sans-serif;
    display: flex;
    align-items: center;
    justify-content: center;
    gap: 60px;
  }
  .card {
    position: relative;
    width: 510px;
    height: 292px;
    background: var(--card);
    border-radius: 3px;
    box-shadow: 0 10px 28px var(--shadow);
    overflow: hidden;
    color: var(--gold);
  }
  .brand {
    position: absolute;
    left: 0; right: 0;
    display: flex;
    align-items: center;
    justify-content: center;
    gap: 10px;
  }
  .brand__mark { width: 12px; height: 12px; background: var(--gold); flex: none; }
  .brand__name { font-weight: 400; line-height: 1; }
  .card--back .brand { top: 130px; }
  .card--back .brand__name { font-size: 28px; }
  .card--front .brand { top: 64px; }
  .card--front .brand__name { font-size: 20px; }
  .card--front .brand__mark { width: 10px; height: 10px; }
  .gold-bar {
    position: absolute;
    height: 28px;
    background: linear-gradient(90deg, var(--gold-deep), var(--gold) 40%, var(--gold-light));
  }
  .gold-bar--top { top: 30px; right: 0; width: 130px; }
  .gold-bar--side { top: 148px; left: 0; width: 190px; }
  .contact {
    position: absolute;
    top: 126px;
    left: 218px;
    font-size: 12.5px;
    line-height: 1.45;
  }
  .contact__name {
    font-weight: 700;
    font-size: 14px;
    letter-spacing: 0.04em;
    margin-bottom: 14px;
  }
  .contact__block + .contact__block { margin-top: 12px; }
</style>
</head>
<body>
  <section class="card card--back" aria-label="Kartenrückseite">
    <div class="brand">
      <span class="brand__mark"></span>
      <span class="brand__name">Ferbin Immobilien</span>
    </div>
  </section>

  <section class="card card--front" aria-label="Kartenvorderseite">
    <div class="gold-bar gold-bar--top"></div>
    <div class="gold-bar gold-bar--side"></div>
    <div class="brand">
      <span class="brand__mark"></span>
      <span class="brand__name">Ferbin Immobilien</span>
    </div>
    <div class="contact">
      <p class="contact__name">LUKAS FERBIN</p>
      <div class="contact__block">
        <p>Talstrasse 7</p>
        <p>6050 Ennetwald</p>
      </div>
      <div class="contact__block">
        <p>+41 79 000 41 18</p>
        <p>info@ferbin-immobilien.ch</p>
      </div>
    </div>
  </section>
</body>
</html>
```